Business price tag design for Furniture Business

Hello,

I have developed a tag for a home furniture business and need 1 more creative template. Please see attachment. I need the template to be very appealing.

Requirements:

1.Tag dimensions needs to be about the same as attached tag.
2. Tag design needs to be suitable for a home furniture business.
3. Tag needs to have locations for the following: Item Title, Now Price, Was Price, Product Number.
4. "The black shape at the bottom of attached tag could be removed.

I have no requirements on colors, but something professional is needed, preferably white background to reduce print ink consumption.

Please see attachment for clarification.

Industry/Entity Type

Retail

Font styles to use
Serif
Sans Serif

Requirements
Must have
• Please see Project Description.
Nice to have

```html
<!DOCTYPE html>
<html lang="en">
<head>
<meta charset="UTF-8">
<title>Price Tag – Hearthwood Home Outlet</title>
<link rel="stylesheet" href="https://fonts.googleapis.com/css2?family=Open+Sans:wght@400;700;800&display=swap">
<style>
  :root {
    --brown: #4a1c04;
    --white: #ffffff;
    --ink: #1a1a1a;
    --price-green: #2d6a10;
    --dots: #6b3a1a;
  }
  html, body {
    margin: 0;
    padding: 0;
    width: 1200px;
    height: 2356px;
    overflow: hidden;
    background: var(--white);
  }
  .tag {
    position: relative;
    width: 1200px;
    height: 2356px;
    font-family: "Open Sans", Arial, sans-serif;
    color: var(--ink);
  }
  .tag-frame {
    position: absolute;
    inset: 0;
  }
  .store-name {
    position: absolute;
    top: 170px;
    left: 112px;
    width: 976px;
    text-align: center;
    font-weight: 700;
    font-size: 66px;
    line-height: 1.2;
    color: var(--white);
    margin: 0;
  }
  .item-title {
    position: absolute;
    left: 118px;
    top: 585px;
    font-size: 82px;
    line-height: 1.2;
    margin: 0;
    font-weight: 400;
  }
  .title-rule {
    position: absolute;
    left: 118px;
    top: 716px;
    width: 696px;
    border-top: 8px dotted var(--dots);
  }
  .product-number {
    position: absolute;
    left: 118px;
    top: 746px;
    font-size: 82px;
    line-height: 1.2;
  }
  .was-price {
    position: absolute;
    left: 118px;
    top: 988px;
    font-size: 114px;
    line-height: 1.2;
  }
  .now-label {
    position: absolute;
    left: 130px;
    top: 1172px;
    font-size: 87px;
    line-height: 1.2;
  }
  .now-price {
    position: absolute;
    left: 436px;
    top: 1180px;
    font-size: 246px;
    line-height: 1;
    font-weight: 800;
    color: var(--price-green);
    letter-spacing: -6px;
  }
  .savings {
    position: absolute;
    left: 132px;
    top: 1682px;
    width: 876px;
    height: 220px;
    border: 12px solid var(--ink);
    display: flex;
    align-items: center;
    justify-content: center;
    font-size: 128px;
    line-height: 1;
  }
</style>
</head>
<body>
  <div class="tag">
    <svg class="tag-frame" width="1200" height="2356" viewBox="0 0 1200 2356" aria-hidden="true">
      <rect x="40" y="40" width="1120" height="2250" fill="var(--brown)"/>
      <rect x="80" y="80" width="1040" height="2170" fill="none" stroke="var(--white)" stroke-width="12"/>
      <path d="M112 2180 L112 550 C 340 370 700 280 1088 244 L1088 2180 Z" fill="var(--white)"/>
    </svg>

    <h1 class="store-name">Hearthwood Home Outlet</h1>

    <h2 class="item-title">Black Queen Bed</h2>
    <div class="title-rule"></div>
    <div class="product-number">B4350</div>

    <div class="was-price">Compare at $500</div>
    <div class="now-label">Only for</div>
    <div class="now-price">$450</div>

    <div class="savings">You save: $50</div>
  </div>
</body>
</html>
```